Travel Company is looking for a STAND OUT Business Card

I need a unique Business Card that will truly stand out. Nothing too busy. Simple is good, right? Not looking for a standard design either. No cookie cutter layout. We are a Travel Company that works more with Companies than Travelers. I had an idea to focus and emphasis on the 2 logo a bit more. This is not necessary, however thought it would look interesting. I am just looking for something interesting and a bit different. Does't have to completely off the wall crazy, just not your run of the mill business card.

Target Market(s)

Hoteliers, Resort Management, Call Centers, Executives, Travelers, Families, Businesses

Industry/Entity Type

Hospitality

Contact Information for Business Card

President/CEO - Marcus T Bellamy (title not necessary if design doesn't allow for it)
contact - (407) 555-0186
email - mbellamy@wayfarenow.example
address - 4812 Quillmore Ave #164
Orlando, FL 32804
website - www.wayfarenow.example

Font styles to use
Serif
Other font styles liked:
• Avenir Next LT Pro BOLD

Requirements
Must have
• simple look and design. Unique design
Nice to have
• I attached the 2 logo separate from the main logo. This can be used separately from the Main Logo, together with the main logo or as main logo. I included the logo font. Use it or not, designers choice.
Should not have
• cookie cutter design. Little use of red other than the logo

```html
<!DOCTYPE html>
<html lang="en">
<head>
<meta charset="utf-8">
<title>Wayfarenow Business Card</title>
<link href="https://fonts.googleapis.com/css2?family=Nunito+Sans:wght@300;400;800&display=swap" rel="stylesheet">
<style>
  :root {
    --stage: #e9eaec;
    --card: #ffffff;
    --ink: #1a1a1a;
    --muted: #6b6b6b;
    --accent: #e32227;
    --edge: #2a2a2a;
  }
  html, body {
    margin: 0;
    padding: 0;
    width: 1200px;
    height: 900px;
    overflow: hidden;
    background: var(--stage);
    font-family: "Nunito Sans", "Avenir Next", sans-serif;
    color: var(--ink);
  }
  .canvas {
    width: 1200px;
    height: 900px;
    display: flex;
    flex-direction: column;
    align-items: center;
    justify-content: center;
    gap: 56px;
  }
  .card {
    position: relative;
    width: 620px;
    height: 354px;
    background: var(--card);
    border-radius: 26px;
    box-shadow: 0 6px 0 var(--edge), 0 14px 30px rgba(0,0,0,0.18);
    box-sizing: border-box;
  }
  .wordmark {
    display: flex;
    align-items: center;
    gap: 10px;
    font-weight: 800;
    color: var(--ink);
    letter-spacing: -0.02em;
  }
  .wordmark__dot {
    border-radius: 50%;
    background: var(--accent);
    flex: none;
  }
  .card--back {
    display: flex;
    align-items: center;
    justify-content: center;
  }
  .card--back .wordmark { font-size: 58px; }
  .card--back .wordmark__dot { width: 30px; height: 30px; }

  .card--front { padding: 34px 40px; }
  .holder__name {
    margin: 0;
    font-size: 30px;
    font-weight: 800;
    line-height: 1.1;
  }
  .holder__title {
    margin: 2px 0 0;
    font-size: 21px;
    font-weight: 300;
    color: var(--muted);
  }
  .contact {
    margin-top: 30px;
    display: grid;
    grid-template-columns: 72px auto;
    row-gap: 7px;
    font-size: 14.5px;
  }
  .contact dt { font-weight: 400; color: var(--ink); }
  .contact dd { margin: 0; font-weight: 400; }
  .card--front .wordmark {
    position: absolute;
    right: 38px;
    bottom: 36px;
    font-size: 34px;
    gap: 8px;
  }
  .card--front .wordmark__dot { width: 18px; height: 18px; }
</style>
</head>
<body>
<main class="canvas">
  <section class="card card--back" aria-label="Card back">
    <div class="wordmark"><span class="wordmark__dot"></span><span>wayfarenow</span></div>
  </section>

  <section class="card card--front" aria-label="Card front">
    <h1 class="holder__name">Marcus T Bellamy</h1>
    <p class="holder__title">President/CEO</p>
    <dl class="contact">
      <dt>Phone</dt><dd>(407) 555-0186</dd>
      <dt>Email</dt><dd>mbellamy@wayfarenow.example</dd>
      <dt>Web</dt><dd>www.wayfarenow.example</dd>
      <dt>Address</dt><dd>4812 Quillmore Ave #164 Orlando, FL 32804</dd>
    </dl>
    <div class="wordmark"><span class="wordmark__dot"></span><span>wayfarenow</span></div>
  </section>
</main>
</body>
</html>
```